R&t subterra

We specialize in CIPP pipe lining but do other underground utilities trenchless as well.

Target Market(s)

Trenchless sewer replacement

Contact Information for Business Card

Doug Falvey 715-482-6170 Plover Falls, wi

```html
<!DOCTYPE html>
<html lang="en">
<head>
<meta charset="utf-8">
<title>R&amp;t subterra – Business Card</title>
<link href="https://fonts.googleapis.com/css2?family=Montserrat:wght@800;900&family=Poppins:wght@600;700&display=swap" rel="stylesheet">
<style>
  :root {
    --backdrop: #5e5e61;
    --blue-deep: #2a7fc4;
    --blue-mid: #2f86c9;
    --blue-light: #3ea3d7;
    --blue-bright: #4aa8e0;
    --brand-emboss: #2377ba;
    --grey-text: #8a8a8c;
    --grey-band: #a2a2a4;
    --rule: #b9b9bb;
    --white: #ffffff;
  }
  * { margin: 0; padding: 0; box-sizing: border-box; }
  html, body {
    width: 900px; height: 1200px; overflow: hidden;
    background: var(--backdrop);
  }
  .canvas { position: relative; width: 900px; height: 1200px; }

  .card {
    position: absolute; left: 135px; width: 632px; height: 358px;
    border-radius: 11px; overflow: hidden;
  }
  .card--front {
    top: 215px;
    background: linear-gradient(120deg, var(--blue-mid), var(--blue-light));
    display: flex; align-items: center; justify-content: center; gap: 14px;
  }
  .card--back { top: 628px; background: var(--white); }

  .brand {
    display: flex; align-items: center; gap: 10px;
    font-family: "Poppins", sans-serif; font-weight: 700;
  }
  .brand__dot { border-radius: 50%; flex: none; }
  .card--front .brand { font-size: 46px; color: var(--brand-emboss); }
  .card--front .brand__dot { width: 54px; height: 54px; background: var(--brand-emboss); }

  .card--back .brand {
    position: absolute; left: 50px; top: 150px;
    font-size: 29px; color: var(--blue-deep);
  }
  .card--back .brand__dot { width: 36px; height: 36px; background: var(--blue-deep); }

  .divider {
    position: absolute; left: 316px; top: 110px;
    width: 1px; height: 134px; background: var(--rule);
  }
  .contact { position: absolute; left: 340px; top: 106px; }
  .contact__name {
    font-family: "Montserrat", sans-serif; font-weight: 900;
    font-size: 28px; line-height: 30px; letter-spacing: 1.5px;
    text-transform: uppercase;
  }
  .contact__first { color: var(--blue-deep); }
  .contact__last { color: var(--blue-bright); }
  .contact__row {
    display: flex; align-items: center; gap: 8px;
    font-family: "Poppins", sans-serif; color: var(--grey-text);
  }
  .contact__row svg { flex: none; }
  .contact__phone { margin-top: 22px; font-size: 19px; font-weight: 700; letter-spacing: 4.5px; }
  .contact__place { margin-top: 8px; font-size: 17px; font-weight: 600; }

  .footer-band { position: absolute; left: 0; bottom: 0; width: 632px; height: 15px; }
</style>
</head>
<body>
<main class="canvas">

  <section class="card card--front" aria-label="Card front">
    <div class="brand"><span class="brand__dot"></span><span>R&amp;t subterra</span></div>
  </section>

  <section class="card card--back" aria-label="Card back">
    <div class="brand"><span class="brand__dot"></span><span>R&amp;t subterra</span></div>
    <div class="divider"></div>
    <div class="contact">
      <p class="contact__name contact__first">Doug</p>
      <p class="contact__name contact__last">Falvey</p>
      <p class="contact__row contact__phone">
        <svg width="17" height="17" viewBox="0 0 24 24" aria-hidden="true"><path fill="#2a7fc4" d="M6.6 10.8a15.1 15.1 0 0 0 6.6 6.6l2.2-2.2c.3-.3.7-.4 1-.2 1.1.4 2.3.6 3.6.6.6 0 1 .4 1 1V20c0 .6-.4 1-1 1A17 17 0 0 1 3 4c0-.6.4-1 1-1h3.5c.6 0 1 .4 1 1 0 1.3.2 2.5.6 3.6.1.3 0 .7-.2 1l-2.3 2.2z"/></svg>
        715-482-6170
      </p>
      <p class="contact__row contact__place">
        <svg width="17" height="22" viewBox="0 0 24 32" aria-hidden="true"><path fill="#3ea3d7" d="M12 0C5.4 0 0 5.3 0 11.9 0 20.8 12 32 12 32s12-11.2 12-20.1C24 5.3 18.6 0 12 0zm0 16.5a4.7 4.7 0 1 1 0-9.4 4.7 4.7 0 0 1 0 9.4z"/></svg>
        Plover Falls, wi
      </p>
    </div>
    <svg class="footer-band" viewBox="0 0 632 15" preserveAspectRatio="none" aria-hidden="true">
      <polygon points="0,0 309,0 299,15 0,15" fill="#a2a2a4"/>
      <polygon points="314,0 632,0 632,15 304,15" fill="#2a7fc4"/>
    </svg>
  </section>

</main>
</body>
</html>
```